Bluestone Advisory & Mgmt - Professional Business Cards

Hi!

I am a Real Estate Developer and Construction Consultant.

I have a lot of inspiration from previous designs and would be open to using the attached Designs as a starting point. I would like to see these styles incorporated into your designs.

I really need professional business card to go with it that includes my important info.

Look forward to seeing your designs!.

Target Market(s)

My Target market are building owners, lawyers, consultants.

Industry/Entity Type

Real Estate Development

Contact Information for Business Card

My Name: Dorian Pelkey
My Title: Principle
Company Name: Bluestone Advisory & Mgmt, LLC
Address: 348 West 71st Street, 9th FL New York, NY 10010
Mobile: 917.806.3971
Website: bam-hvx.example

Font styles to use
Serif
Sans Serif

Colors

Designer to choose colors to be used in the design.

Requirements
Must have
• Must incorporate the logo attached or have new that looks similar.
• Must use professional font that will be seen and judged by wealthy land owners and developers.
• Must incorporate some of the color green.
Should not have
• Photo's or pictures of people or buildings of any kind.

```html
<!DOCTYPE html>
<html lang="en">
<head>
<meta charset="utf-8">
<title>Bluestone Advisory &amp; Mgmt - Business Cards</title>
<link rel="stylesheet" href="https://fonts.googleapis.com/css2?family=Montserrat:wght@400;500;600&display=swap">
<style>
  :root {
    --bg: #e9eaea;
    --card-white: #ffffff;
    --brand-green: #4cb87a;
    --accent-green: #3aad66;
    --text-grey: #8e8a8a;
    --logo-grey: #9d9797;
    --white: #ffffff;
  }
  * { margin: 0; padding: 0; box-sizing: border-box; }
  html, body {
    width: 1200px; height: 900px; overflow: hidden;
    background: var(--bg);
    font-family: "Montserrat", Arial, sans-serif;
  }
  .canvas {
    position: relative; width: 1200px; height: 900px;
    display: flex; align-items: center; justify-content: center; gap: 40px;
  }
  .card {
    width: 520px; height: 297px; position: relative;
    box-shadow: 0 6px 18px rgba(0,0,0,0.12);
  }
  .card--front { background: var(--card-white); display: flex; align-items: center; padding: 0 30px; }
  .card--back { background: var(--brand-green); display: flex; align-items: center; justify-content: center; }

  .wordmark { display: flex; align-items: center; gap: 10px; }
  .wordmark__dot { width: 14px; height: 14px; border-radius: 50%; background: var(--accent-green); flex: none; }
  .wordmark__name { font-weight: 500; line-height: 1.15; color: var(--accent-green); }
  .card--front .wordmark__name { font-size: 25px; width: 180px; }
  .card--back .wordmark__dot { background: var(--white); width: 18px; height: 18px; }
  .card--back .wordmark__name { color: var(--white); font-size: 34px; width: 260px; }

  .divider { width: 1.5px; height: 170px; background: var(--accent-green); margin: 0 26px 0 20px; flex: none; }

  .contact { color: var(--text-grey); font-size: 13px; line-height: 1.45; }
  .contact__name { color: var(--accent-green); font-weight: 600; font-size: 19px; letter-spacing: 0.5px; text-transform: uppercase; }
  .contact__title { font-size: 13px; margin-bottom: 12px; }
  .contact__address { margin-bottom: 10px; }
  .contact__row { display: flex; align-items: center; gap: 8px; }
  .contact__row svg { width: 10px; height: 10px; flex: none; }
</style>
</head>
<body>
<main class="canvas">
  <section class="card card--front">
    <div class="wordmark">
      <span class="wordmark__dot"></span>
      <span class="wordmark__name">Bluestone Advisory Management</span>
    </div>
    <div class="divider"></div>
    <div class="contact">
      <div class="contact__name">Dorian Pelkey</div>
      <div class="contact__title">Principle</div>
      <div class="contact__address">348 West 71st Street,<br>9th FL New York, NY 10010</div>
      <div class="contact__row">
        <svg viewBox="0 0 10 10"><path d="M2 0.5 L3.8 0.5 L4.3 3 L3 3.8 Q4 6 6.2 7 L7 5.7 L9.5 6.2 L9.5 8 Q9.5 9.5 8 9.5 Q1 9 0.5 2 Q0.5 0.5 2 0.5Z" fill="#3aad66"/></svg>
        <span>917.806.3971</span>
      </div>
      <div class="contact__row">
        <svg viewBox="0 0 10 10"><rect x="0.5" y="2" width="9" height="6.5" fill="none" stroke="#3aad66" stroke-width="1.2"/><path d="M0.5 2 L5 5.5 L9.5 2" fill="none" stroke="#3aad66" stroke-width="1.2"/></svg>
        <span>info@bam-hvx.example</span>
      </div>
      <div class="contact__row">
        <svg viewBox="0 0 10 10"><circle cx="5" cy="5" r="4.4" fill="none" stroke="#3aad66" stroke-width="1.1"/><path d="M0.6 5 H9.4 M5 0.6 Q2 5 5 9.4 M5 0.6 Q8 5 5 9.4" fill="none" stroke="#3aad66" stroke-width="0.9"/></svg>
        <span>www.bam-hvx.example</span>
      </div>
    </div>
  </section>

  <section class="card card--back">
    <div class="wordmark">
      <span class="wordmark__dot"></span>
      <span class="wordmark__name">Bluestone Advisory Management</span>
    </div>
  </section>
</main>
</body>
</html>
```